Attractive Flyer for Moving Company

Our Company called "Harborlight Moving Company".
We provide moving service for home and businesses
We need a flyer for a moving company, located in San Diego, CA USA
Flyer size will be 7 x 5 inches, double sided.

Flyer needs to be very attractive and catchy for eye. I want people to keep it even if they dont need our service. I attached a lot of text in separate word file.
Logo, brief and additional pictures are attached.

Target Market(s)

27 years - 55 Years old

Industry/Entity Type

Moving Company

Colors
ec1f27
3176b5
ffffff

Requirements
Must have
• Attached in Word File
Nice to have
• Please be creative in placing a text and selecting a back ground picture.

```html
<!DOCTYPE html>
<html lang="en">
<head>
<meta charset="utf-8">
<title>Harborlight Moving Company – Flyer</title>
<link href="https://fonts.googleapis.com/css2?family=Open+Sans:ital,wght@0,400;0,600;0,700;0,800;1,400;1,600&display=swap" rel="stylesheet">
<style>
  :root{
    --red:#ec1f27;
    --brick:#b01c22;
    --rust:#b7341f;
    --blue:#3176b5;
    --navy:#1f5a98;
    --orange:#f47d12;
    --sky:#dbe6f1;
    --white:#ffffff;
    --ink:#1d3557;
    --dark:#2a2a2a;
  }
  *{box-sizing:border-box;margin:0;padding:0}
  html,body{width:1132px;height:1200px;overflow:hidden}
  body{background:var(--dark);font-family:"Open Sans",sans-serif;position:relative}
  .flyer{position:absolute;width:793px;height:566px;background:var(--sky);overflow:hidden}
  .flyer--front{left:170px;top:27px}
  .flyer--back{left:170px;top:616px}
  .abs{position:absolute}

  .brand{left:24px;top:14px;width:150px;text-align:center;color:var(--brick)}
  .brand__name{font-weight:700;font-size:19px;line-height:1.05}
  .brand__sub{font-weight:700;font-size:12px;letter-spacing:.5px}
  .brand__tagline{font-style:italic;font-size:8px;color:#222;margin-top:6px;line-height:1.25}
  .brand__license{font-size:7px;color:#222;margin-top:2px}
  .badge-circle{left:176px;top:75px;width:36px;height:36px;border-radius:50%;background:#b8321f}
  .badge-square{left:221px;top:73px;width:25px;height:41px;background:var(--navy);border:2px solid var(--white);outline:1px solid var(--navy)}

  .headline{left:330px;top:10px;width:370px;text-align:right;color:var(--brick)}
  .headline__title{font-weight:700;font-size:31px;line-height:1.1;text-align:center}
  .headline__sub{font-weight:600;font-size:14.5px;line-height:1.1;padding-right:14px}

  .diagonal{left:0;top:0}
  .photo{border-radius:2px}

  .need{left:29px;top:140px;color:var(--rust);font-weight:700;font-size:42px;line-height:1}
  .need__note{left:30px;top:185px;color:var(--brick);font-size:8px;font-weight:600;line-height:1.25}

  .section-title{color:var(--navy);font-weight:700;font-size:17px}
  .checklist{list-style:none;font-size:8.6px;color:var(--ink)}
  .checklist li{height:16px;line-height:16px;padding-left:14px;position:relative}
  .checklist li::before{content:"";position:absolute;left:2px;top:4px;width:3px;height:6px;border:solid var(--navy);border-width:0 1.6px 1.6px 0;transform:rotate(45deg)}

  .footer{left:0;top:526px;width:793px;height:40px;display:flex;color:var(--white)}
  .footer__web{width:259px;background:var(--blue);display:flex;align-items:center;justify-content:center;font-size:16px;font-weight:600}
  .footer__phone{width:274px;background:var(--rust);display:flex;align-items:center;justify-content:center;gap:10px;font-size:26px;font-weight:700}
  .footer__place{flex:1;background:var(--blue);display:flex;align-items:center;justify-content:center;font-size:16px;font-weight:600}

  .save{left:29px;top:150px;width:404px;height:40px;background:var(--red);color:var(--white);font-weight:700;font-size:27px;line-height:40px;padding-left:5px;clip-path:polygon(0 0,96% 0,100% 100%,0 100%)}
  .save-fold{left:396px;top:190px}
  .ribbon-blue{left:489px;top:227px;width:304px;height:40px;background:var(--blue);color:var(--white);font-weight:600;font-size:14px;line-height:14px;text-align:right;padding:6px 36px 0 0;clip-path:polygon(0 0,100% 0,100% 100%,8% 100%)}
  .ribbon-fold{left:513px;top:267px}

  .price{left:29px;color:var(--white);padding:9px 0 0 4px;line-height:1}
  .price__label{font-weight:600;font-size:13.5px}
  .price__value{font-weight:700;font-size:19px;margin-top:1px}
  .price--blue{top:282px;width:190px;height:51px;background:var(--blue);clip-path:polygon(0 0,88% 0,100% 50%,88% 100%,0 100%)}
  .price--red{top:334px;width:208px;height:52px;background:var(--red);clip-path:polygon(0 0,88% 0,100% 50%,88% 100%,0 100%);padding-left:1px}
  .price--orange{top:389px;width:222px;height:59px;background:var(--orange);clip-path:polygon(0 0,89% 0,100% 50%,89% 100%,0 100%);padding-left:1px;padding-top:12px}
</style>
</head>
<body>

<!-- FRONT -->
<section class="flyer flyer--front">
  <svg class="abs diagonal" width="793" height="566" aria-hidden="true"><polygon points="187,526 793,157 793,526" fill="#ffffff"/></svg>

  <div class="abs brand">
    <div class="brand__name">Harborlight</div>
    <div class="brand__sub">Moving Company</div>
    <div class="brand__tagline">"Quality Focused,<br>Customer Recommended Movers"</div>
    <div class="brand__license">Licensed &amp; Fully Insured</div>
  </div>
  <div class="abs badge-circle"></div>
  <div class="abs badge-square"></div>

  <div class="abs headline">
    <div class="headline__title">Harborlight Moving Company</div>
    <div class="headline__sub">We porvide Professional Moving Service</div>
  </div>

  <div class="abs need">Need MOVERS</div>
  <div class="abs need__note">Not moving soon? Keep this flyer for later and/or share it with friends.<br>Promotion is valid until January 1st, 2019)</div>

  <div class="abs section-title" style="left:29px;top:232px">Moving Services:</div>
  <ul class="abs checklist" style="left:27px;top:257px">
    <li>Residntial</li><li>Long Distance</li><li>Commercial</li>
    <li>Loading/ Unloading rental Truck</li><li>Portable Storage</li><li>Packing Service</li>
  </ul>

  <div class="abs section-title" style="left:29px;top:369px">Why Call Us?</div>
  <ul class="abs checklist" style="left:27px;top:396px">
    <li>Customer Oriented Service</li><li>Years of Great reputation (Lots of 5 Star Reviews)</li>
    <li>Affordable pricing</li><li>Professional, efficient, strong movers</li>
    <li>We always handle your belongings with care</li><li>Clean and equipped trucks</li>
    <li>Absolutely NO surprising fees</li>
  </ul>

  <div class="abs photo" role="img" aria-label="White box truck beside a stopwatch and a stack of cardboard moving boxes" style="left:250px;top:205px;width:543px;height:232px;background:linear-gradient(90deg,#e4e6e8 0%,#cfd3d6 35%,#b9bcbf 48%,#d6b27e 62%,#c99a5e 100%)"></div>

  <div class="abs footer">
    <div class="footer__web">www.HarborlightMoving.com</div>
    <div class="footer__phone">
      <svg width="20" height="20" viewBox="0 0 24 24" aria-hidden="true"><path fill="#7fb4e6" d="M6.6 10.8a15.1 15.1 0 0 0 6.6 6.6l2.2-2.2c.3-.3.7-.4 1-.2 1.1.4 2.3.6 3.6.6.6 0 1 .4 1 1V20c0 .6-.4 1-1 1A17 17 0 0 1 3 4c0-.6.4-1 1-1h3.5c.6 0 1 .4 1 1 0 1.2.2 2.4.6 3.6.1.3 0 .7-.2 1z"/></svg>
      1-855-555-0142
    </div>
    <div class="footer__place">Located in San Diego, CA</div>
  </div>
</section>

<!-- BACK -->
<section class="flyer flyer--back">
  <div class="abs brand">
    <div class="brand__name">Harborlight</div>
    <div class="brand__sub">Moving Company</div>
    <div class="brand__tagline">"Quality Focused,<br>Customer Recommended Movers"</div>
    <div class="brand__license">Licensed &amp; Fully Insured</div>
  </div>
  <div class="abs badge-circle"></div>
  <div class="abs badge-square"></div>

  <div class="abs headline">
    <div class="headline__title">Harborlight Moving Company</div>
    <div class="headline__sub">We porvide Professional Moving Service</div>
  </div>

  <div class="abs save">SAVE 15% -25% on your move</div>
  <svg class="abs save-fold" width="37" height="18" aria-hidden="true"><polygon points="0,18 37,0 0,0" fill="#26384a"/></svg>

  <div class="abs photo" role="img" aria-label="White cargo van with open doors and two figures carrying a small house into it" style="left:289px;top:256px;width:496px;height:268px;background:linear-gradient(100deg,#dbe6f1 0%,#c9ccd2 25%,#aeb2b8 50%,#b8743f 70%,#d2d2d2 90%,#dbe6f1 100%)"></div>

  <div class="abs ribbon-blue">We Move Homes, Appartments<br>Offices &amp; Storage</div>
  <svg class="abs ribbon-fold" width="24" height="17" aria-hidden="true"><polygon points="0,0 24,0 10,17" fill="#26384a"/></svg>

  <div class="abs price price--blue"><div class="price__label">3 hours of Moving Service</div><div class="price__value">$235</div></div>
  <div class="abs price price--red"><div class="price__label">3 hours of Moving Service</div><div class="price__value">$325</div></div>
  <div class="abs price price--orange"><div class="price__label">Boxes and Packing supplies</div><div class="price__value">20% OFF</div></div>

  <div class="abs footer">
    <div class="footer__web">www.HarborlightMoving.com</div>
    <div class="footer__phone">
      <svg width="20" height="20" viewBox="0 0 24 24" aria-hidden="true"><path fill="#7fb4e6" d="M6.6 10.8a15.1 15.1 0 0 0 6.6 6.6l2.2-2.2c.3-.3.7-.4 1-.2 1.1.4 2.3.6 3.6.6.6 0 1 .4 1 1V20c0 .6-.4 1-1 1A17 17 0 0 1 3 4c0-.6.4-1 1-1h3.5c.6 0 1 .4 1 1 0 1.2.2 2.4.6 3.6.1.3 0 .7-.2 1z"/></svg>
      1-855-555-0142
    </div>
    <div class="footer__place">Located in San Diego, CA</div>
  </div>
</section>

</body>
</html>
```